Brindle Pet Shop Homepage

We are a pet shop, we focus on dog food / cat food / rodents & bird food

Based on WooCommerce

It should be a simple but professional homepage with an informative start page. In the shop it should then be possible to shop for products/manufacturers etc. Navigation/Filter menu on the left would be ideal.

Next menus:
ABOUT US
CONTACT
DOG
CAT
HOLDER

My Account - Login
My Cart

Footer:
Conditions
payment options
social media

In addition to our logo, I have attached 2 example pages from another shop which we would use as a guideline.

Target Market(s)

pet store

Industry/Entity Type

Animal, Pet Shop

Coding

Coded - Design and coding required

Number of Pages Required

1 page

Font styles to use
Sans Serif

Colors
0054AA
0677BA
7BADD7
CADEEF
E8F1F8

Requirements
Must have
• Main Page, Contact, About Us, Shop, Check Out, Member Login, Mailchimp Marketing - We work with WooCommerce

```html
<!DOCTYPE html>
<html lang="en">
<head>
<meta charset="utf-8">
<title>Brindle Pet Shop</title>
<link href="https://fonts.googleapis.com/css2?family=Montserrat:ital,wght@0,400;0,500;0,600;0,700;0,800;1,400;1,800&family=Open+Sans:wght@400;600&display=swap" rel="stylesheet">
<style>
:root{
  --blue-dark:#0054AA;
  --blue:#0677BA;
  --blue-mid:#7BADD7;
  --blue-light:#CADEEF;
  --blue-pale:#E8F1F8;
  --ink:#111111;
  --text:#333333;
  --muted:#777777;
  --star:#F4A300;
  --footer:#0E0E0E;
}
*{margin:0;padding:0;box-sizing:border-box}
html,body{width:1200px;height:4874px;overflow:hidden}
body{position:relative;background:#fff;font-family:"Montserrat",sans-serif;color:var(--text)}
.abs{position:absolute}
.ph{position:absolute;z-index:0}
.btn{position:absolute;z-index:2;background:var(--blue-dark);color:#fff;font-weight:700;font-size:13px;border-radius:18px;display:flex;align-items:center;justify-content:center;letter-spacing:.3px}
.section-title{position:absolute;left:0;width:1200px;text-align:center;font-weight:700;font-size:33px;color:var(--ink);letter-spacing:.5px}

/* top bar */
.topbar{left:0;top:0;width:1200px;height:36px;background:var(--blue-dark);color:#fff;font-size:11px}
.search{left:98px;top:6px;width:190px;height:24px;border:1px solid #fff;border-radius:12px;padding-left:12px;line-height:22px}
.social-top{left:300px;top:9px;display:flex;gap:10px}
.social-top span{width:11px;height:11px;background:#fff;border-radius:2px;display:block}
.track{left:846px;top:11px}
.user{left:972px;top:6px;width:24px;height:24px;border:1px solid #fff;border-radius:50%}
.cart{left:1014px;top:6px;width:84px;height:24px;border:1px solid #fff;border-radius:12px;text-align:center;line-height:22px}

/* nav */
.nav{left:0;top:36px;width:1200px;height:59px;background:#fff;border-bottom:1px solid #eee}
.nav a{position:absolute;top:23px;font-size:14px;font-weight:500;color:var(--ink);text-decoration:none}
.logo{left:480px;top:6px;width:240px;text-align:center}
.logo .mark{display:inline-flex;align-items:center;gap:8px;font-weight:800;font-size:22px;color:var(--blue-dark)}
.logo .mark i{width:22px;height:22px;border-radius:50%;background:var(--blue-dark);display:block}
.logo .tag{font-size:11px;color:var(--blue);letter-spacing:1.5px;margin-top:1px}

/* hero */
.hero{left:0;top:95px;width:1200px;height:564px;background:linear-gradient(180deg,var(--blue-light),#a9c9e6);overflow:hidden}
.hero h1{position:absolute;z-index:2;left:102px;top:160px;font-size:66px;font-weight:600;color:var(--ink);letter-spacing:1px}
.hero p{position:absolute;z-index:2;left:102px;top:252px;width:400px;font-size:14px;line-height:25px;color:#222}
.dots{left:102px;top:390px;display:flex;gap:14px;z-index:2}
.dots span{width:11px;height:11px;border:1.5px solid #fff;border-radius:50%}
.dots span.on{background:#fff}

/* category cards */
.cat-card{position:absolute;top:725px;width:320px;height:212px;background:var(--blue-light);overflow:hidden}
.cat-card h3{position:absolute;z-index:2;left:14px;top:44px;font-size:29px;font-weight:500;color:var(--ink);line-height:28px}
.cat-card p{position:absolute;z-index:2;left:14px;font-size:12px;color:#222}
.cat-card .btn{left:14px;width:98px;height:34px;font-size:12px}

/* tabs */
.tab{position:absolute;top:1058px;height:31px;border:1px solid #555;font-size:13px;font-weight:500;color:var(--ink);display:flex;align-items:center;justify-content:center}
.tab.active{background:var(--blue-dark);border-color:var(--blue-dark);color:#fff}

/* product cards */
.product{position:absolute;width:239px;height:284px;background:#fff;box-shadow:0 0 6px rgba(0,0,0,.12)}
.product .pack{position:absolute;left:62px;top:18px;width:115px;height:170px;border-radius:6px}
.product h4{position:absolute;left:14px;top:210px;font-size:13.5px;font-weight:600;color:var(--ink)}
.product .rate{position:absolute;left:14px;top:233px;font-size:12px;color:var(--star);letter-spacing:1px}
.product .rate em{font-style:normal;color:var(--muted);font-size:11px;letter-spacing:0;margin-left:4px}
.product .price{position:absolute;left:14px;top:254px;font-size:15px;font-weight:700;color:var(--blue)}

/* sale */
.sale{left:0;top:1776px;width:1200px;height:437px;background:linear-gradient(90deg,var(--blue-light),#bcd5ec);overflow:hidden}
.sale .kicker{position:absolute;z-index:2;left:119px;top:90px;font-size:17px;color:var(--ink)}
.sale h2{position:absolute;z-index:2;left:119px;top:116px;font-size:54px;line-height:50px;font-weight:800;font-style:italic;color:var(--ink)}
.sale p{position:absolute;z-index:2;left:119px;top:240px;width:390px;font-size:14px;line-height:26px;color:#222}

/* arrows */
.arrow{position:absolute}

/* about */
.about-text{left:0;top:2783px;width:596px;height:431px;background:#F4F4F4}
.about-text h2{position:absolute;left:100px;top:84px;font-size:33px;font-weight:700;color:var(--ink)}
.about-text p{position:absolute;left:100px;top:136px;width:458px;font-family:"Open Sans",sans-serif;font-size:14.6px;line-height:24.4px;text-align:justify;color:#333}

/* testimonials */
.testi{left:0;top:3214px;width:1200px;height:453px;background:linear-gradient(180deg,var(--blue-dark),var(--blue))}
.testi .section-title{top:46px;color:#fff}
.quote-box{position:absolute;top:123px;width:415px;height:256px;border:1px solid rgba(255,255,255,.5)}
.quote-box .qm{position:absolute;left:30px;top:-6px}
.quote-box p{position:absolute;left:26px;top:58px;width:370px;font-size:13.5px;line-height:29px;font-style:italic;color:#fff}
.quote-box .avatar{position:absolute;left:26px;top:176px;width:48px;height:48px;border-radius:50%;background:#cfd8e3}
.quote-box .who{position:absolute;left:86px;top:184px;color:#fff}
.quote-box .who b{display:block;font-size:15px;font-weight:700}
.quote-box .who span{font-size:12px}

/* blog */
.blog{position:absolute;top:3797px;width:318px}
.blog .img{position:relative;width:318px;height:203px}
.blog .date{position:absolute;z-index:2;left:129px;top:175px;width:60px;height:60px;border-radius:50%;background:var(--blue-dark);border:3px solid #fff;color:#fff;text-align:center;line-height:1}
.blog .date b{display:block;font-size:21px;margin-top:10px}
.blog .date span{font-size:9px;font-weight:600}
.blog h4{position:absolute;top:252px;width:318px;text-align:center;font-size:18px;font-weight:600;color:var(--ink)}
.blog p{position:absolute;top:286px;left:19px;width:280px;text-align:center;font-family:"Open Sans",sans-serif;font-size:13.5px;line-height:24px;color:var(--muted)}

/* gallery */
.gallery-title{left:0;top:4196px;width:1200px;display:flex;justify-content:center;align-items:center;gap:12px;font-size:30px;font-weight:700;color:var(--ink)}
.gallery-title i{width:26px;height:26px;border:3px solid var(--ink);border-radius:6px;display:block}
.shot{position:absolute;top:4259px;width:240px;height:275px}

/* footer */
.footer{left:0;top:4538px;width:1200px;height:336px;background:var(--footer);color:#fff}
.fcol{position:absolute;top:64px}
.fcol h5{font-size:13px;font-weight:700;letter-spacing:.5px;margin-bottom:18px}
.fcol li{list-style:none;font-size:13px;line-height:28.5px;color:#e6e6e6}
.fcol .lead{font-size:13px;line-height:19px;color:#e6e6e6;width:280px}
.email{margin-top:16px;width:265px;height:35px;border:1px solid #fff;font-size:12px;padding-left:10px;line-height:33px;position:relative}
.email svg{position:absolute;right:10px;top:10px}
.fsocial{display:flex;gap:10px;margin-top:26px}
.fsocial span{width:34px;height:34px;border:1.5px solid #fff;border-radius:50%;display:block}
.copy{left:100px;top:303px;font-size:12px;color:#e6e6e6}
.pay{top:296px;width:44px;height:28px;border-radius:3px}
</style>
</head>
<body>

<!-- top bar -->
<div class="abs topbar">
  <div class="abs search">Search
    <svg class="abs" style="right:10px;top:6px" width="11" height="11" viewBox="0 0 11 11"><circle cx="4.5" cy="4.5" r="3.5" fill="none" stroke="#fff" stroke-width="1.5"/><line x1="7" y1="7" x2="10" y2="10" stroke="#fff" stroke-width="1.5"/></svg>
  </div>
  <div class="abs social-top"><span></span><span></span><span></span><span></span></div>
  <div class="abs track">
    <svg width="8" height="10" viewBox="0 0 8 10" style="vertical-align:-1px"><path d="M4 0a4 4 0 0 1 4 4c0 3-4 6-4 6S0 7 0 4a4 4 0 0 1 4-4z" fill="#fff"/><circle cx="4" cy="4" r="1.5" fill="#0054AA"/></svg>
    Track My Order</div>
  <div class="abs user"></div>
  <div class="abs cart">Cart (0)</div>
</div>

<!-- navigation -->
<nav class="abs nav">
  <a style="left:98px">HOME</a>
  <a style="left:200px">ABOUT US</a>
  <a style="left:335px">DOG</a>
  <div class="abs logo">
    <div class="mark"><i></i>Brindle Pet</div>
    <div class="tag">PREMIUM PET FOOD</div>
  </div>
  <a style="left:818px">CAT</a>
  <a style="left:907px">HOLDER</a>
  <a style="left:1022px">CONTACT</a>
</nav>

<!-- hero -->
<section class="abs hero">
  <svg class="abs" style="left:700px;top:45px" width="560" height="560" viewBox="0 0 560 560"><circle cx="300" cy="300" r="250" fill="none" stroke="var(--blue)" stroke-width="46"/></svg>
  <div class="ph" role="img" aria-label="Food packs with a grey kitten and a small dog eating from a metal bowl" style="left:540px;top:130px;width:660px;height:434px;background:linear-gradient(90deg,rgba(255,255,255,0) 0%,#d7c6a8 25%,#c9a46c 70%,rgba(255,255,255,0) 100%);opacity:.85;border-radius:40px 40px 0 0"></div>
  <h1>BRINDLE PET</h1>
  <p>Lorem ipsum dolor sit amet, consectetur adipiscing elit, sed do eiusmod tempor incididunt ut</p>
  <div class="btn" style="left:102px;top:321px;width:127px;height:34px">SHOP NOW</div>
  <div class="abs dots"><span></span><span class="on"></span><span></span><span></span></div>
</section>

<!-- category cards -->
<div class="cat-card" style="left:100px">
  <div class="ph" role="img" aria-label="Dog sitting between two food bowls" style="left:200px;top:10px;width:120px;height:202px;background:linear-gradient(180deg,#d9b993,#a8875f)"></div>
  <h3>Dog Food</h3><p style="top:93px">Finibus Bonorum et Malor</p>
  <div class="btn" style="top:124px">SHOP NOW</div>
</div>
<div class="cat-card" style="left:439px">
  <div class="ph" role="img" aria-label="Kitten beside a bowl of dry food" style="left:205px;top:10px;width:115px;height:202px;background:linear-gradient(180deg,#b9b3a6,#8c7d68)"></div>
  <h3>Cat Food</h3><p style="top:93px">Finibus Bonorum et Malor</p>
  <div class="btn" style="top:124px">SHOP NOW</div>
</div>
<div class="cat-card" style="left:778px">
  <div class="ph" role="img" aria-label="Blue tit perched over a pile of bird seed" style="left:200px;top:30px;width:120px;height:182px;background:linear-gradient(180deg,#9fb7c8,#b79a63)"></div>
  <h3 style="top:34px">Rodents &amp;<br>Bird food</h3><p style="top:93px">Finibus Bonorum et Malor</p>
  <div class="btn" style="top:124px">SHOP NOW</div>
</div>

<!-- products -->
<h2 class="section-title" style="top:1002px">OUR PRODUCTS</h2>
<div class="tab active" style="left:265px;width:110px">ALL</div>
<div class="tab" style="left:382px;width:112px">DOG FOOD</div>
<div class="tab" style="left:502px;width:113px">CAT FOOD</div>
<div class="tab" style="left:623px;width:110px">CAT FOOD</div>
<div class="tab" style="left:740px;width:195px">RODENTS &amp; BIRD FOOD</div>

<div class="product" style="left:100px;top:1117px"><div class="pack ph" role="img" aria-label="Red dog food bag" style="background:linear-gradient(160deg,#c9343a,#8e1c22)"></div><h4>Finibus Bonorum et Malor</h4><div class="rate">★★★★★<em>(5 Reviews)</em></div><div class="price">$30.50</div></div>
<div class="product" style="left:354px;top:1117px"><div class="pack ph" role="img" aria-label="Teal cat food bag and kraft food pouch" style="background:linear-gradient(120deg,#3f9a8f,#c9c7b4)"></div><h4>Finibus Bonorum et Malor</h4><div class="rate">★★★★★<em>(5 Reviews)</em></div><div class="price">$30.50</div></div>
<div class="product" style="left:606px;top:1117px"><div class="pack ph" role="img" aria-label="Green dog food bag" style="background:linear-gradient(160deg,#a9d33a,#6ea21d)"></div><h4>Finibus Bonorum et Malor</h4><div class="rate">★★★★★<em>(5 Reviews)</em></div><div class="price">$30.50</div></div>
<div class="product" style="left:859px;top:1117px"><div class="pack ph" role="img" aria-label="Yellow dog food bag" style="background:linear-gradient(160deg,#f4c21c,#e0861a)"></div><h4>Finibus Bonorum et Malor</h4><div class="rate">★★★★★<em>(5 Reviews)</em></div><div class="price">$30.50</div></div>

<div class="product" style="left:100px;top:1414px"><div class="pack ph" role="img" aria-label="Purple cat food bag" style="background:linear-gradient(160deg,#7a3f8c,#4c1f5e)"></div><h4>Finibus Bonorum et Malor</h4><div class="rate">★★★★★<em>(5 Reviews)</em></div><div class="price">$30.50</div></div>
<div class="product" style="left:354px;top:1414px"><div class="pack ph" role="img" aria-label="Kraft paper dog food pouch" style="background:linear-gradient(160deg,#d8c29a,#b59a6c)"></div><h4>Finibus Bonorum et Malor</h4><div class="rate">★★★★★<em>(5 Reviews)</em></div><div class="price">$30.50</div></div>
<div class="product" style="left:606px;top:1414px"><div class="pack ph" role="img" aria-label="Yellow cat food bag" style="background:linear-gradient(160deg,#f2d64a,#e3a23a)"></div><h4>Finibus Bonorum et Malor</h4><div class="rate">★★★★★<em>(5 Reviews)</em></div><div class="price">$30.50</div></div>
<div class="product" style="left:859px;top:1414px"><div class="pack ph" role="img" aria-label="Red dog food bag" style="background:linear-gradient(160deg,#c9343a,#8e1c22)"></div><h4>Finibus Bonorum et Malor</h4><div class="rate">★★★★★<em>(5 Reviews)</em></div><div class="price">$30.50</div></div>

<!-- sale banner -->
<section class="abs sale">
  <div class="ph" role="img" aria-label="Brown dog and white cat beside food bags, tins and trays" style="left:530px;top:50px;width:670px;height:387px;background:linear-gradient(90deg,#c27a3c 0%,#e7e2dc 45%,#d9d4d2 75%,#bfc3c9 100%);border-radius:30px 30px 0 0"></div>
  <div class="kicker">Available On Store</div>
  <h2>Sale Off Up<br>To 50%</h2>
  <p>Lorem ipsum dolor sit amet, consectetur adipiscing elit, sed do eiusmod tempor incididunt ut</p>
  <div class="btn" style="left:119px;top:308px;width:127px;height:34px">SHOP NOW</div>
</section>

<!-- best seller -->
<h2 class="section-title" style="top:2280px">BEST SELLER</h2>
<svg class="arrow" style="left:44px;top:2474px" width="38" height="24" viewBox="0 0 38 24"><circle cx="24" cy="12" r="11" fill="none" stroke="#222" stroke-width="1.8"/><line x1="2" y1="12" x2="30" y2="12" stroke="#222" stroke-width="1.8"/><polyline points="8,6 2,12 8,18" fill="none" stroke="#222" stroke-width="1.8"/></svg>
<svg class="arrow" style="left:1117px;top:2474px" width="38" height="24" viewBox="0 0 38 24"><circle cx="14" cy="12" r="11" fill="none" stroke="#222" stroke-width="1.8"/><line x1="8" y1="12" x2="36" y2="12" stroke="#222" stroke-width="1.8"/><polyline points="30,6 36,12 30,18" fill="none" stroke="#222" stroke-width="1.8"/></svg>
<div class="product" style="left:100px;top:2347px"><div class="pack ph" role="img" aria-label="Red dog food bag" style="background:linear-gradient(160deg,#c9343a,#8e1c22)"></div><h4>Finibus Bonorum et Malor</h4><div class="rate">★★★★★<em>(5 Reviews)</em></div><div class="price">$30.50</div></div>
<div class="product" style="left:354px;top:2347px"><div class="pack ph" role="img" aria-label="Kraft paper dog food pouch" style="background:linear-gradient(160deg,#d8c29a,#b59a6c)"></div><h4>Finibus Bonorum et Malor</h4><div class="rate">★★★★★<em>(5 Reviews)</em></div><div class="price">$30.50</div></div>
<div class="product" style="left:606px;top:2347px"><div class="pack ph" role="img" aria-label="Green dog food bag" style="background:linear-gradient(160deg,#a9d33a,#6ea21d)"></div><h4>Finibus Bonorum et Malor</h4><div class="rate">★★★★★<em>(5 Reviews)</em></div><div class="price">$30.50</div></div>
<div class="product" style="left:859px;top:2347px"><div class="pack ph" role="img" aria-label="Red dog food bag" style="background:linear-gradient(160deg,#c9343a,#8e1c22)"></div><h4>Finibus Bonorum et Malor</h4><div class="rate">★★★★★<em>(5 Reviews)</em></div><div class="price">$30.50</div></div>

<!-- about -->
<section class="abs about-text">
  <h2>ABOUT US</h2>
  <p>Sed ut perspiciatis unde omnis iste natus error sit voluptatem accusantium doloremque laudantium, totam rem aperiam, eaque ipsa quae ab illo inventore veritatis et quasi architecto beatae vitae dicta sunt explicabo. Nemo enim ipsam voluptatem quia voluptas sit aspernatur aut odit aut fugit, sed quia consequuntur magni dolores eos qui ratione voluptatem sequi nesciunt. Neque porro quisquam est, qui dolorem ipsum quia dolor sit amet, consectetur, adipisci velit, sed quia non numquam eius modi tempora incidunt ut labore et dolore magnam aliquam quaerat voluptatem. Ut enim ad</p>
</section>
<div class="ph" role="img" aria-label="Woman with a white dog beside a food sack and bowl" style="left:596px;top:2783px;width:604px;height:431px;background:linear-gradient(100deg,#6f8aa8 0%,#b7b9b8 40%,#ded8cf 70%,#c8bdb0 100%)"></div>

<!-- testimonials -->
<section class="abs testi">
  <h2 class="section-title">WHAT PEOPLE SAYS</h2>
  <svg class="arrow" style="left:100px;top:223px" width="28" height="50" viewBox="0 0 28 50"><polyline points="26,2 2,25 26,48" fill="none" stroke="#fff" stroke-width="2"/></svg>
  <svg class="arrow" style="left:1070px;top:223px" width="28" height="50" viewBox="0 0 28 50"><polyline points="2,2 26,25 2,48" fill="none" stroke="#fff" stroke-width="2"/></svg>
  <div class="quote-box" style="left:172px">
    <svg class="qm" width="58" height="46" viewBox="0 0 58 46"><path d="M0 0h24v22L14 46H4l8-24H0z M32 0h24v22L46 46H36l8-24H32z" fill="#fff"/></svg>
    <p>Sed ut perspiciatis unde omnis iste or sit voluptatem accusantium doloremque laudtotam rem aperiam, eaque ipsa quae ab illo inventoris et quasi arceaae dicta sunt explicabo.</p>
    <div class="avatar ph" role="img" aria-label="Customer portrait"></div>
    <div class="who"><b>LUKAS BERG</b><span>Bonorum et</span></div>
  </div>
  <div class="quote-box" style="left:613px">
    <svg class="qm" width="58" height="46" viewBox="0 0 58 46"><path d="M0 0h24v22L14 46H4l8-24H0z M32 0h24v22L46 46H36l8-24H32z" fill="#fff"/></svg>
    <p>Sed ut perspiciatis unde omnis iste or sit voluptatem accusantium doloremque laudtotam rem aperiam, eaque ipsa quae ab illo inventoris et quasi arceaae dicta sunt explicabo.</p>
    <div class="avatar ph" role="img" aria-label="Customer portrait"></div>
    <div class="who"><b>LUKAS BERG</b><span>Bonorum et</span></div>
  </div>
</section>

<!-- blog -->
<h2 class="section-title" style="top:3732px">LATEST BLOG</h2>
<article class="blog" style="left:100px">
  <div class="img" role="img" aria-label="Bowl of dog treats" style="background:linear-gradient(160deg,#6b5a45,#2f5f93)"></div>
  <div class="date"><b>30</b><span>JULY</span></div>
  <h4>Finibus Bonorum et Malorum</h4>
  <p>Sed ut perspiciatis unde omnis iste natus error sit voluatem accusantium doloremque laudantium,</p>
</article>
<article class="blog" style="left:441px">
  <div class="img" role="img" aria-label="Dog running on a beach" style="background:linear-gradient(180deg,#a9bfd2,#c9a36e)"></div>
  <div class="date"><b>30</b><span>JULY</span></div>
  <h4>Finibus Bonorum eMalorum</h4>
  <p>Sed ut perspiciatis unde omnis iste natus error sit voluatem accusantium doloremque laudantium,</p>
</article>
<article class="blog" style="left:782px">
  <div class="img" role="img" aria-label="Dried chew treats" style="background:linear-gradient(160deg,#f1efec,#6e4a30)"></div>
  <div class="date"><b>30</b><span>JULY</span></div>
  <h4>Finibus Bonorum eMalorum</h4>
  <p>Sed ut perspiciatis unde omnis iste natus error sit voluatem accusantium doloremque laudantium,</p>
</article>

<!-- gallery -->
<div class="abs gallery-title"><i></i>BRINDLE PET</div>
<div class="shot ph" role="img" aria-label="Long-haired collie" style="left:0;background:linear-gradient(160deg,#b07a45,#5b3a22)"></div>
<div class="shot ph" role="img" aria-label="Stack of dog biscuits" style="left:240px;background:linear-gradient(160deg,#b49a83,#d8d2cc)"></div>
<div class="shot ph" role="img" aria-label="Husky" style="left:480px;background:linear-gradient(160deg,#3a3a3c,#a9a9ab)"></div>
<div class="shot ph" role="img" aria-label="Pet food trays" style="left:720px;background:linear-gradient(160deg,#eef1f4,#c9d7e6)"></div>
<div class="shot ph" role="img" aria-label="Grey cat eating from a bowl" style="left:960px;background:linear-gradient(160deg,#5d5a58,#9b9795)"></div>

<!-- footer -->
<footer class="abs footer">
  <div class="fcol" style="left:98px"><h5>INFORMATION</h5><ul><li>Home</li><li>About Us</li><li>Contact Us</li><li>Press Releases</li></ul></div>
  <div class="fcol" style="left:333px"><h5>HELP &amp; SUPPORT</h5><ul><li>Help Desk</li><li>PO Quality Clauses</li><li>FAQ/Help</li><li>Privacy Policy</li><li>Terms &amp; Conditions</li><li>Site Map</li></ul></div>
  <div class="fcol" style="left:602px"><h5>MY ACCOUNT</h5><ul><li>My Cart</li><li>Wishlist</li><li>Order History</li><li>Returns</li><li>Shipping</li></ul></div>
  <div class="fcol" style="left:833px"><h5>JOIN THE FINE CREW</h5>
    <div class="lead">Insider info on new arrivals, early access, and everything fine.</div>
    <div class="email">Your Email<svg width="14" height="14" viewBox="0 0 14 14"><path d="M1 7L13 1 9 13 7 8z" fill="#fff"/></svg></div>
    <div class="fsocial"><span></span><span></span><span></span><span></span></div>
  </div>
  <div class="abs copy">© Copyright 2023 Brindle Pet. All Rights Reserved</div>
  <div class="abs pay" style="left:900px;background:#e9eef5"></div>
  <div class="abs pay" style="left:951px;background:#3a4a63"></div>
  <div class="abs pay" style="left:1002px;background:#f2f2f2"></div>
  <div class="abs pay" style="left:1054px;background:#2f7fd1"></div>
</footer>

</body>
</html>
```